Minimalist Professional Business Card Design

We will be revamping our marketing materials: Business cards, Website and Catalogs.
Our Overall Design direction is to have a Minimalist artwork with Professionalism and Premium feel. The revamp starts with the new business card design followed by the others. Thus the designer whom work is selected for this job will likely to follow through with the subsequent jobs.

Target Market(s)

Upscale

Industry/Entity Type

Manufacturing

Contact Information for Business Card

For the Business Cards, the following are required:
. Minimalist yet Professional and Premium Feel
. Background Colors: white and / or light pastel yellow and if needed to smoothen the yellow, the light grey can be incorporated. We are changing our corporate bright yellow to either one of the three alternatives:
1. Soylant yellow CMYK (1%, 0%, 52%, 3%)
2. Popcorn yellow CMYK (0%, 0%, 33%, 0%)
3. Papaya yellow CMYK (0%, 0%, 51%, 0%)

Information to be inputed in the business cards:

Name: Barlen Moritova
Position: Managing Director

Company's name: Vellomar Valves Pte. Ltd.
Address: 512 Halvick Lane #07-09B
Singapore 617302
Tel: (65) 6281 4096
Fax: (65) 6294 7118
Email: barlen@vellomarvalves-example.com
Website: www.vellomarvalves-example.com
Skype: Vellomar.Valves
Whatsapp/ Line/ Viber/ WeChat: (65) 9372 6081

Company's Logo
Company's Slogan
Two product photos placed side by side (if this gets into the way of the design, it is OK not to include them)

Font styles to use
Serif

Colors
ffffff

Requirements
Must have
• Minimalist
Should not have
• Messy, crowded, playful

```html
<!DOCTYPE html>
<html lang="en">
<head>
<meta charset="utf-8">
<title>Vellomar Valves – Business Card Layout</title>
<link rel="stylesheet" href="https://fonts.googleapis.com/css2?family=Noto+Serif:wght@400;700&family=Courgette&display=swap">
<style>
  :root {
    --paper: #ffffff;
    --canvas: #ffffff;
    --ink-dark: #333333;
    --ink-text: #3a3a3a;
    --ink-muted: #666666;
    --accent-yellow: #f2e600;
    --tab-grey: #e4e4e4;
    --line-grey: #d9d9d9;
    --sheet-edge: #dddddd;
  }
  * { box-sizing: border-box; margin: 0; padding: 0; }
  html, body {
    width: 1200px; height: 1000px; overflow: hidden;
    background: var(--canvas);
    font-family: "Noto Serif", Georgia, serif;
    color: var(--ink-text);
  }
  .sheet {
    position: absolute; left: 172px; top: 378px;
    width: 856px; height: 244px;
    border: 1px solid var(--sheet-edge);
    background: var(--paper);
  }
  .card-back, .card-front { position: absolute; top: 0; height: 100%; }

  /* Back: contact panel + name panel */
  .card-back { left: 0; width: 428px; }
  .contact-panel { position: absolute; left: 0; top: 0; width: 246px; height: 100%; background: var(--paper); }
  .name-panel { position: absolute; left: 246px; top: 0; width: 182px; height: 100%; background: var(--ink-dark); }
  .tab {
    position: absolute; background: var(--tab-grey);
    border-radius: 0 0 10px 10px;
  }
  .contact-panel .tab { left: 26px; top: 0; width: 50px; height: 88px; }
  .side-rule { position: absolute; left: 235px; top: 48px; width: 11px; height: 136px; background: var(--tab-grey); }

  .brand { position: absolute; display: flex; align-items: center; gap: 6px; }
  .brand-mark { width: 18px; height: 18px; border-radius: 50%; background: var(--ink-muted); flex: none; }
  .brand-name { font-weight: 700; font-size: 13px; letter-spacing: 0.5px; color: var(--ink-muted); }
  .contact-panel .brand { left: 32px; top: 51px; }

  .contact-list { position: absolute; left: 25px; top: 143px; font-size: 6.6px; line-height: 9.6px; color: var(--ink-text); list-style: none; }
  .contact-list .company { font-weight: 700; font-size: 7.6px; margin-bottom: 2px; }

  .person-name { font-weight: 700; color: var(--paper); font-size: 14px; }
  .person-name .surname { color: var(--accent-yellow); }
  .name-panel .person-name { position: absolute; left: 35px; top: 45px; }
  .name-panel .role { position: absolute; left: 35px; top: 65px; font-size: 8px; font-weight: 700; color: var(--accent-yellow); }
  .product-photo {
    position: absolute; left: 65px; top: 162px; width: 51px; height: 50px;
    background: linear-gradient(90deg, #f4f4f4, #cfcfcf 50%, #f4f4f4);
    border: 3px solid var(--paper);
  }

  /* Front */
  .card-front { left: 428px; width: 428px; background: var(--paper); }
  .card-front .tab { left: 188px; top: 0; width: 50px; height: 40px; }
  .front-identity { position: absolute; left: 125px; top: 72px; display: flex; align-items: center; gap: 14px; }
  .front-identity .brand { position: static; flex-direction: column; gap: 4px; }
  .front-identity .brand-mark { width: 22px; height: 22px; }
  .front-identity .brand-name { font-size: 11px; }
  .front-name { font-weight: 700; font-size: 14px; color: var(--ink-dark); }
  .front-name .surname { font-weight: 400; }
  .front-role { font-size: 8px; font-weight: 700; color: var(--ink-muted); margin-top: 3px; }
  .ledge { position: absolute; left: 95px; top: 194px; width: 240px; height: 8px; background: var(--tab-grey); }
  .slogan-band {
    position: absolute; left: 0; bottom: 0; width: 100%; height: 42px;
    background: var(--ink-dark); display: flex; align-items: center; justify-content: center;
    font-family: "Courgette", cursive; color: var(--paper); font-size: 13px; padding-left: 24px;
  }
  .slogan-divider { width: 1px; height: 20px; background: var(--paper); margin: 0 9px; }
</style>
</head>
<body>
  <main class="sheet">
    <section class="card-back">
      <div class="contact-panel">
        <div class="tab"></div>
        <div class="brand"><span class="brand-mark"></span><span class="brand-name">VELLOMAR</span></div>
        <ul class="contact-list">
          <li class="company">Company’s name: Vellomar Valves Pte. Ltd.</li>
          <li>Address: 512 Halvick Lane #07-09B</li>
          <li>Singapore 617302</li>
          <li>Tel: (65) 6281 4096</li>
          <li>Fax: (65) 6294 7118</li>
          <li>Email: barlen@vellomarvalves-example.com</li>
          <li>Website: www.vellomarvalves-example.com</li>
          <li>Skype: Vellomar.Valves</li>
          <li>Whatsapp/ Line/ Viber/ WeChat: (65) 9372 6081</li>
        </ul>
        <div class="side-rule"></div>
      </div>
      <div class="name-panel">
        <p class="person-name">Barlen <span class="surname">Moritova</span></p>
        <p class="role">Managing Director</p>
        <div class="product-photo" role="img" aria-label="Product photo of a stainless steel valve"></div>
      </div>
    </section>

    <section class="card-front">
      <div class="tab"></div>
      <div class="front-identity">
        <div class="brand"><span class="brand-mark"></span><span class="brand-name">VELLOMAR</span></div>
        <div>
          <p class="front-name">Barlen <span class="surname">Moritova</span></p>
          <p class="front-role">Managing Director</p>
        </div>
      </div>
      <div class="ledge"></div>
      <div class="slogan-band">
        <span>Made With Pride</span><span class="slogan-divider"></span><span>For Heavy Duty</span>
      </div>
    </section>
  </main>
</body>
</html>
```